Local Motorsports Photography Business Card Design

Looking for a Logo and Business Card design for my father who is a local photographer based in Perth operating under the business name "KLR Photography". Specializing in Motorsports (Torque Racers/Hyperwheels/Corvan Trial) and events photography.
Would like it to look professional, while still maintaining a local/personal feel. Color\Design of the Logo and Card are open to your own interpretation, but should limit the color scheme to around 2-3 colors.
Design should be a logo one side and contact details on the rear. The website currently is very simple and a generic template and should not be used as a basis for design.
Industry/Entity Type
Business
Contact Information for Business Card
Name: Malcolm Purdie
Website: www.klrphotography-example.com.au
Email: malcolm@klrphotography-example.com.au
Phone: 0471 629 385
Look and feel
Each slider illustrates characteristics of the customer's brand and the style your logo design should communicate.

```html
<!DOCTYPE html>
<html lang="en">
<head>
<meta charset="utf-8">
<title>KLR Photography – Business Card</title>
<link rel="stylesheet" href="https://fonts.googleapis.com/css2?family=Exo+2:wght@400;500;600&display=swap">
<style>
  :root {
    --green: #1b9a4b;
    --lime: #8dc63f;
    --white: #ffffff;
    --paper: #f4f5f4;
    --backdrop: #e6e8e6;
    --mark: #cfe8c2;
  }
  * { box-sizing: border-box; margin: 0; padding: 0; }
  html, body { width: 1200px; height: 900px; overflow: hidden; }
  body {
    background: var(--backdrop);
    font-family: "Exo 2", Arial, sans-serif;
    position: relative;
  }
  .card {
    position: absolute;
    left: 280px;
    width: 640px;
    height: 366px;
    border-radius: 30px;
    overflow: hidden;
    background: linear-gradient(135deg, var(--white), var(--paper));
    box-shadow: 0 6px 18px rgba(0,0,0,.12);
  }
  .card--front { top: 54px; }
  .card--back { top: 480px; }
  .panel { position: absolute; inset: 0; }
  .details {
    position: absolute;
    left: 30px;
    top: 34px;
    color: var(--white);
  }
  .details__name {
    font-size: 21px;
    font-weight: 500;
    letter-spacing: 1px;
    text-transform: uppercase;
    line-height: 26px;
  }
  .details__role { font-size: 14px; line-height: 18px; }
  .details__address {
    font-size: 13px;
    line-height: 18px;
    margin: 24px 0 0 20px;
  }
  .contact-list { list-style: none; margin-top: 16px; }
  .contact-list li {
    display: flex;
    align-items: center;
    gap: 8px;
    font-size: 11px;
    line-height: 20px;
    white-space: nowrap;
  }
  .contact-list svg { width: 12px; height: 12px; flex: none; }
  .brand {
    position: absolute;
    display: flex;
    align-items: center;
    gap: 10px;
  }
  .card--front .brand { right: 34px; top: 190px; }
  .card--back .brand { left: 50%; top: 50%; transform: translate(-50%, -50%); }
  .brand__name {
    font-size: 24px;
    font-weight: 500;
    letter-spacing: 1px;
    color: var(--green);
    white-space: nowrap;
  }
  .brand__dot {
    width: 44px;
    height: 44px;
    border-radius: 50%;
    background: var(--mark);
    flex: none;
  }
</style>
</head>
<body>

<section class="card card--front">
  <svg class="panel" viewBox="0 0 640 366" width="640" height="366">
    <path fill="var(--green)" d="M0 0 H350 Q320 200 270 366 H0 Z"/>
    <path fill="var(--lime)" d="M358 0 H370 Q340 200 290 366 H278 Q328 200 358 0 Z"/>
  </svg>
  <div class="details">
    <p class="details__name">Malcolm Purdie</p>
    <p class="details__role">Managing Director</p>
    <p class="details__address">27 Kerr Street<br>Landsdale Perth WA</p>
    <ul class="contact-list">
      <li><svg viewBox="0 0 12 12"><path fill="#fff" d="M2 1 L4 1 L5 4 L3.6 5 Q4.8 7.4 7 8.4 L8 7 L11 8 L11 10 Q11 11 10 11 Q1 10 1 2 Q1 1 2 1Z"/></svg>0471 629 385</li>
      <li><svg viewBox="0 0 12 12"><rect x="3" y="0.5" width="6" height="11" rx="1" fill="none" stroke="#fff" stroke-width="1.2"/></svg>0471 629 385</li>
      <li><svg viewBox="0 0 12 12"><rect x="1" y="4" width="10" height="6" rx="1" fill="#fff"/><rect x="3" y="1" width="6" height="3" fill="#fff"/></svg>08 9324 1170</li>
      <li><svg viewBox="0 0 12 12"><rect x="1" y="2.5" width="10" height="7" rx="1" fill="none" stroke="#fff" stroke-width="1.1"/><path d="M1.5 3 L6 6.5 L10.5 3" fill="none" stroke="#fff" stroke-width="1"/></svg>malcolm@klrphotography-example.com.au</li>
      <li><svg viewBox="0 0 12 12"><circle cx="6" cy="6" r="5" fill="none" stroke="#fff" stroke-width="1.2"/><path d="M1 6 H11 M6 1 Q3 6 6 11 M6 1 Q9 6 6 11" fill="none" stroke="#fff" stroke-width="0.9"/></svg>www.klrphotography-example.com.au</li>
    </ul>
  </div>
  <div class="brand">
    <span class="brand__name">KLR PHOTOGRAPHY</span>
    <span class="brand__dot" role="img" aria-label="Motorcycle racer illustration area"></span>
  </div>
</section>

<section class="card card--back">
  <div class="brand">
    <span class="brand__name">KLR PHOTOGRAPHY</span>
    <span class="brand__dot" role="img" aria-label="Motorcycle racer illustration area"></span>
  </div>
</section>

</body>
</html>
```